Elmrow Management real estate management company needs presentation folder to hand clients

looking for a folder with pockets that represent my real estate management company when i hand to client reports or promotional material. I only do resedential real estate. I want classy and professional - pictures or additioal graphixs are fine

when a client open i will usally insert text and reports about my business
also on the inside flap is usally place for my business card i will upload a picture so the theme can be constant

Target Market(s)

my existing real estate cleints
and i will use when i am soliciting new business

Industry/Entity Type

Real Estate

Font styles to use
Serif

Requirements
Must have
• must have logo
• must give appearance of professionalism and maturity
• have basic company info tel# ,address
• id like viewer to know I manage real estate - focus on residential small to large apartment buildings
• not strip malls, not giganic complexes - im a mid size company
• logo is black but i welcome color as u see fit
Nice to have
• maybe pictures
• my slogan - " we will manage your building like its our own "
• focus on professioanl, safe, trust worthy
• type style should be clear and readable - but im open to sugestions

```html
<!DOCTYPE html>
<html lang="en">
<head>
<meta charset="utf-8">
<title>Elmrow Management – Presentation Folder</title>
<link href="https://fonts.googleapis.com/css2?family=Open+Sans:wght@400;600;700&display=swap" rel="stylesheet">
<style>
  :root {
    --ink: #000000;
    --paper: #ffffff;
    --fold-line: #7a7a7a;
  }
  html, body {
    margin: 0;
    padding: 0;
    width: 1200px;
    height: 999px;
    overflow: hidden;
    background: var(--paper);
  }
  .folder {
    position: relative;
    width: 1200px;
    height: 999px;
    font-family: "Open Sans", Arial, sans-serif;
  }
  .folder__spread {
    position: absolute;
    left: 30px;
    top: 47px;
    width: 1140px;
    height: 658px;
    background: var(--ink);
    border-bottom: 1px solid var(--fold-line);
  }
  .contact {
    position: absolute;
    left: 62px;
    top: 580px;
    color: var(--paper);
    font-size: 9.5px;
    line-height: 12.5px;
    letter-spacing: -0.2px;
    font-weight: 600;
  }
  .contact p { margin: 0; }
  .contact .contact__address {
    margin-top: 7px;
    font-size: 9px;
    letter-spacing: -0.3px;
  }
  .cover {
    position: absolute;
    left: 620px;
    top: 64px;
    width: 535px;
    height: 623px;
    background: var(--paper);
  }
  .cover__frame {
    position: absolute;
    left: 7px;
    top: 8px;
    right: 7px;
    bottom: 7px;
    border: 4px solid var(--ink);
  }
  .cover__name {
    position: absolute;
    left: 0;
    right: 0;
    top: 304px;
    text-align: center;
    font-size: 30px;
    font-weight: 700;
    color: var(--ink);
    letter-spacing: 0.5px;
    display: flex;
    align-items: center;
    justify-content: center;
    gap: 12px;
  }
  .cover__name-mark {
    width: 18px;
    height: 18px;
    background: var(--ink);
  }
  .cover__slogan {
    position: absolute;
    left: 0;
    right: 0;
    top: 561px;
    text-align: center;
    font-size: 20.5px;
    font-weight: 600;
    color: var(--ink);
    margin: 0;
  }
  .pockets {
    position: absolute;
    left: 0;
    top: 0;
  }
</style>
</head>
<body>
<main class="folder">
  <section class="folder__spread">
    <div class="contact">
      <p>Office tel: 914-555-0142</p>
      <p>email: hello@elmrowmgmt.com</p>
      <p>Cell: 917-555-0178</p>
      <p class="contact__address">24 ALDER COURT SUITE 210 MAPLEWOOD NY 10500</p>
    </div>
  </section>

  <section class="cover">
    <div class="cover__frame"></div>
    <div class="cover__name"><span class="cover__name-mark"></span>Elmrow Management</div>
    <p class="cover__slogan">we will manage your building like its our own</p>
  </section>

  <svg class="pockets" width="1200" height="999" viewBox="0 0 1200 999" aria-hidden="true">
    <path class="pocket pocket--left" fill="#000" d="M78 706 H597 L567 890 Q560 951 527 951 H78 Z"/>
    <path class="pocket pocket--right" fill="#000" d="M605 706 H1122 V951 H675 Q642 951 634 890 Z"/>
  </svg>
</main>
</body>
</html>
```